High impact classy folder for an HVAC and Electrical contractor

We need a folder designed. It needs to be high impact and classy with a rich look to it. We want to cement our branding via the use of the folder so the look will need to have impact with use of our logo and colors.

We want to pull the entire brand look and feel together with this folder. We are going to be making other marketing materials and this is the start of a much larger project. In the ideal situation the winning desginer will continue on with the rest of the projects because they will know how to apply the brand look.

We want to give our local company the feel of a national franchise. Wherein the brand is very prominent and is repeated over and over again.

Use of logo and color scheme will be important.

We like dark backgrounds because they really make the logo pop.

Target Market(s)

homeowners

Font styles to use
Serif

Requirements
Must have
• Logo prominent on the front
• Our Tag Line:
• The Best Way To Live In New Jersey Is With Harbor Vale"
• On the inside pockets:
• Our Phone number: 555-214-6873
• A message to our customers:
• We want to thank you for choosing Harbor Vale Services today
• Our name says it all, because for over 30 years we have prided ourselves on delivering the best service and exceeding our customers' expectations everyday. Whether you need something fixed, replaced or upgraded, no matter how large or small, the dedicated and experts at Harbor Vale Services are here to take care of you. Delivering the right solution for you the first time- everytime - and ensuring you are always 100% satisfied. If for any reason you want to speak with us, please do not hesitate to call or email. Thank you again for choosing Harbor Vale Services.
• On the rear: a graphic that says 24-7 service
• A list of other services we provide:
• Solar
• Generators
• Home Security
• Home Automation
• Home Inspection
• Energy Audits
• 1 Day Bathroom remodles
• Basement Waterproofing
• Garage Doors
• Home Theaters
Nice to have
• I added photos of a flyer and of a mobile website to give an idea of the color scheme as well

```html
<!DOCTYPE html>
<html lang="en">
<head>
<meta charset="utf-8">
<title>Harbor Vale Services — Presentation Folder</title>
<link rel="stylesheet" href="https://fonts.googleapis.com/css2?family=Cinzel:wght@600&family=Open+Sans:wght@400;600&family=Roboto+Condensed:wght@700&display=swap">
<style>
  :root {
    --stage: #b7c4d9;
    --navy: #243657;
    --navy-deep: #1d2c49;
    --navy-soft: #2e4470;
    --cream: #efe3c2;
    --orange: #f08a24;
    --paper: #ffffff;
    --paper-shade: #e9ebee;
    --silver: #c9ccd1;
    --logo-gray: #8d8f93;
    --ink-light: #ffffff;
    --card: #222326;
  }
  * { box-sizing: border-box; margin: 0; padding: 0; }
  html, body { width: 1200px; height: 847px; overflow: hidden; }
  body { background: var(--stage); position: relative; font-family: "Open Sans", sans-serif; }

  .panel { position: absolute; top: 190px; width: 350px; height: 467px; overflow: hidden; }

  /* Front cover */
  .front-cover { left: 60px; background: var(--paper-shade); }
  .front-cover__shape { position: absolute; inset: 0; }
  .front-cover__artwork {
    position: absolute; left: 40px; top: 20px; width: 260px; height: 310px; border-radius: 50%;
    background: radial-gradient(circle, rgba(70,110,170,.35) 0%, rgba(70,110,170,.12) 60%, rgba(70,110,170,0) 75%);
  }
  .front-cover__name {
    position: absolute; left: 0; right: 0; top: 120px; text-align: center;
    font-family: "Cinzel", serif; font-weight: 600; font-size: 34px; line-height: 1.15; color: var(--cream);
  }
  .front-cover__tagline {
    position: absolute; left: 0; right: 0; bottom: 10px; text-align: center;
    font-family: "Cinzel", serif; font-weight: 600; font-size: 11.5px; color: var(--navy);
  }

  /* Inside spread */
  .inside-left { left: 460px; background: var(--paper); }
  .inside-right { left: 810px; background: var(--paper-shade); }
  .inside__name {
    position: absolute; left: 0; right: 0; top: 115px; text-align: center;
    font-family: "Cinzel", serif; font-weight: 600; font-size: 32px; line-height: 1.15; color: var(--logo-gray);
  }
  .pocket {
    position: absolute; left: 0; right: 0; bottom: 0; height: 160px; background: var(--navy);
    border-top: 2px solid var(--navy-soft);
  }
  .pocket__message { padding: 14px 20px 0 78px; color: var(--ink-light); }
  .pocket__heading { font-size: 7.5px; font-weight: 600; color: var(--orange); margin-bottom: 4px; }
  .pocket__body { font-size: 5.2px; line-height: 1.75; }
  .pocket__call {
    margin-top: 8px; font-family: "Roboto Condensed", sans-serif; font-weight: 700; font-size: 25px; color: var(--ink-light);
  }
  .pocket__call span { color: var(--orange); }

  .business-card {
    position: absolute; left: 70px; top: 38px; width: 150px; height: 88px; background: var(--card);
    display: flex; align-items: center; justify-content: center; gap: 6px;
    box-shadow: 3px 4px 0 #111;
  }
  .business-card::before, .business-card::after {
    content: ""; position: absolute; left: 0; right: 0; height: 4px; background: var(--orange);
  }
  .business-card::before { top: 8px; }
  .business-card::after { bottom: 8px; }
  .business-card__mark { width: 8px; height: 8px; background: var(--ink-light); }
  .business-card__name { font-size: 11px; font-weight: 600; color: var(--ink-light); }
</style>
</head>
<body>

  <section class="panel front-cover">
    <svg class="front-cover__shape" viewBox="0 0 350 467" width="350" height="467">
      <defs>
        <linearGradient id="crewTone" x1="0" y1="0" x2="1" y2="1">
          <stop offset="0" stop-color="#c7ccd6"/>
          <stop offset="0.5" stop-color="#5b6478"/>
          <stop offset="1" stop-color="#2a2e38"/>
        </linearGradient>
      </defs>
      <path d="M0 0 H350 V240 C300 290 170 300 90 360 C45 395 15 420 0 445 Z" fill="var(--navy)"/>
      <path d="M35 435 C75 370 170 335 260 305 C305 290 335 275 350 262 V430 H35 Z" fill="url(#crewTone)" role="img" aria-label="Photo of the service team in uniforms"/>
      <line x1="0" y1="436" x2="350" y2="436" stroke="var(--silver)" stroke-width="1"/>
    </svg>
    <div class="front-cover__artwork" role="img" aria-label="Faint home-service tool icons behind the company name"></div>
    <h1 class="front-cover__name">Harbor Vale<br>Services</h1>
    <p class="front-cover__tagline">The Best Way To Live In New Jersey Is With Harbor Vale</p>
  </section>

  <section class="panel inside-left">
    <p class="inside__name">Harbor Vale<br>Services</p>
    <div class="pocket">
      <div class="pocket__message">
        <h2 class="pocket__heading">We want to thank you for choosing Harbor Vale Services today</h2>
        <p class="pocket__body">Our name says it all, because for over 30 years we have prided ourselves on delivering the best service and exceeding our customers' expectations everyday. Whether you need something fixed, replaced or upgraded, no matter how large or small, the dedicated and experts at Harbor Vale Services are here to take care of you. Delivering the right solution for you the first time- everytime - and ensuring you are always 100% satisfied. If for any reason you want to speak with us, please do not hesitate to call or email. Thank you again for choosing Harbor Vale Services.</p>
        <p class="pocket__call">Call Us <span>555-214-6873</span></p>
      </div>
    </div>
  </section>

  <section class="panel inside-right">
    <p class="inside__name">Harbor Vale<br>Services</p>
    <div class="pocket">
      <div class="business-card">
        <span class="business-card__mark"></span>
        <span class="business-card__name">Papercrest Folders</span>
      </div>
    </div>
  </section>

</body>
</html>
```